Tech business card design

We need an amazing business card design for our new business 'Vantry' a marketing tech startup based in Sydney, Australia. We provide an online marketplace for businesses to search and buy advertising media, connect with service providers and learn more about marketing. We wish to communicate 'cool tech', reliability and professionalism and design based around our logo.

Target Market(s)

Business Owners

Contact Information for Business Card

Name
Position
Email Address
Website
Phone Number

Font styles to use
Other font styles liked:
• Avenir & Avenir Next

Colors

Designer to choose colors to be used in the design.

```html
<!DOCTYPE html>
<html lang="en">
<head>
<meta charset="utf-8">
<title>Vantry Business Card</title>
<link href="https://fonts.googleapis.com/css2?family=Exo+2:wght@400;600;800&display=swap" rel="stylesheet">
<style>
  :root {
    --backdrop: #e9e9ea;
    --card-light: #efefef;
    --card-dark: #211f45;
    --ink-navy: #221f45;
    --ink-white: #ffffff;
    --rule: rgba(255, 255, 255, 0.55);
  }
  * { margin: 0; padding: 0; box-sizing: border-box; }
  html, body {
    width: 1200px;
    height: 800px;
    overflow: hidden;
    background: var(--backdrop);
    font-family: "Exo 2", sans-serif;
  }
  .canvas {
    position: relative;
    width: 1200px;
    height: 800px;
  }
  .card {
    position: absolute;
    top: 278px;
    width: 418px;
    height: 240px;
  }
  .card--front {
    left: 142px;
    background: var(--card-light);
    display: flex;
    align-items: center;
    justify-content: center;
  }
  .card--back {
    left: 638px;
    background: var(--card-dark);
    color: var(--ink-white);
  }
  .wordmark {
    font-family: "Exo 2", sans-serif;
    font-weight: 800;
    letter-spacing: -1px;
    line-height: 1;
  }
  .card--front .wordmark {
    font-size: 80px;
    color: var(--ink-navy);
  }
  .card--back .wordmark {
    position: absolute;
    left: 28px;
    top: 92px;
    font-size: 50px;
    color: var(--ink-white);
  }
  .divider {
    position: absolute;
    left: 208px;
    top: 61px;
    width: 1px;
    height: 123px;
    background: var(--rule);
  }
  .contact {
    position: absolute;
    left: 224px;
    top: 66px;
  }
  .contact__name {
    font-weight: 600;
    font-size: 19px;
    line-height: 20px;
  }
  .contact__role {
    font-weight: 400;
    font-size: 17px;
    line-height: 18px;
    margin-bottom: 10px;
  }
  .contact__line {
    font-weight: 400;
    font-size: 17px;
    line-height: 20px;
  }
</style>
</head>
<body>
  <main class="canvas">
    <section class="card card--front">
      <div class="wordmark">vantry</div>
    </section>
    <section class="card card--back">
      <div class="wordmark">vantry</div>
      <div class="divider"></div>
      <div class="contact">
        <p class="contact__name">Alex Morgan</p>
        <p class="contact__role">manager</p>
        <p class="contact__line">012 345 6789</p>
        <p class="contact__line">your@email.com</p>
        <p class="contact__line">www.website.com</p>
      </div>
    </section>
  </main>
</body>
</html>
```